Need simple and modern looking business card with all my information on one side and logo on the other side
Info :
Company name - VELMAR CONSTRUCTION LLC
Company addres- 418 harbor 87th. Dunmoor park ny 10352
Email- velmarllc@tridomail.Com
Company phone number 555-318-6094
Cell number- 555-742-0583
Web site - velmarllc.Com
My name Gerald tomasino

Target Market(s)

Construction , home improvement, remodeling

Industry/Entity Type

Construction

Contact Information for Business Card

It has to be moder but at the same time simple

Font styles to use
Sans Serif

Colors
0255a3
ffffff
000000
f78f20
b1b1b1
9d9d9d
1b1b1b
33a6d7
ec1f27

Requirements
Must have
• My logo on one side maybe with a some kind of background on the other side all my information
Nice to have
• Some kind of background pictures provided by you .PLEASE HAVE ACCOUNT WITH PIXELVAULT WILL NOT PAY ANY EXTRA FEES .
Should not have
• Any kind of hamer, nails,screws, helmets itp. Please do not copy the other designs come up with something new.

```html
<!DOCTYPE html>
<html lang="en">
<head>
<meta charset="utf-8">
<title>Velmar Construction LLC – Business Card</title>
<link rel="stylesheet" href="https://fonts.googleapis.com/css2?family=Raleway:wght@500;600;700;800&display=swap">
<style>
  :root {
    --card-black: #231f20;
    --orange: #f78f20;
    --orange-light: #f9a62a;
    --white: #ffffff;
    --stage: #b7b08a;
    --stage-low: #9fb59a;
  }
  * { margin: 0; padding: 0; box-sizing: border-box; }
  html, body { width: 1200px; height: 856px; overflow: hidden; }
  body {
    background: linear-gradient(180deg, var(--stage) 0%, var(--stage-low) 100%);
    font-family: "Raleway", Arial, sans-serif;
    position: relative;
  }
  .card {
    position: absolute;
    width: 560px;
    height: 320px;
    border-radius: 24px;
    background: var(--card-black);
    overflow: hidden;
    box-shadow: 0 14px 30px rgba(0,0,0,.28);
  }
  .card--front { left: 580px; top: 70px; }
  .card--back { left: 70px; top: 460px; }

  .accent-glow {
    position: absolute;
    inset: 0;
    background: radial-gradient(ellipse 75% 60% at 15% 0%, rgba(247,143,32,.55) 0%, rgba(249,166,42,.18) 45%, rgba(35,31,32,0) 75%);
  }

  .brand {
    position: absolute;
    display: flex;
    align-items: center;
    gap: 12px;
    color: var(--white);
    font-weight: 600;
    letter-spacing: .06em;
    line-height: 1.15;
  }
  .brand__mark { width: 16px; height: 16px; background: var(--orange); flex: none; }
  .card--front .brand { right: 40px; bottom: 46px; font-size: 26px; }
  .card--back .brand { right: 30px; top: 150px; font-size: 19px; }

  .contact {
    position: absolute;
    left: 34px;
    top: 40px;
    color: var(--white);
    font-size: 17px;
    font-weight: 500;
  }
  .contact__name {
    color: var(--orange);
    font-weight: 800;
    font-size: 21px;
    letter-spacing: .03em;
    text-transform: uppercase;
  }
  .contact__row { display: flex; align-items: center; gap: 8px; }
  .contact__address { margin-top: 26px; line-height: 1.3; }
  .contact__phones { margin-top: 26px; line-height: 1.45; font-size: 19px; }
  .icon { width: 18px; height: 18px; flex: none; }

  .web-band {
    position: absolute;
    left: 0; right: 0; bottom: 0;
    height: 58px;
    background: linear-gradient(90deg, var(--orange) 0%, var(--orange-light) 100%);
    display: flex;
    align-items: center;
    justify-content: center;
    gap: 10px;
    color: var(--white);
    font-weight: 800;
    font-size: 20px;
    letter-spacing: .02em;
  }
</style>
</head>
<body>

  <section class="card card--front" aria-label="Card front">
    <div class="accent-glow" role="img" aria-label="Decorative orange accent across the upper card"></div>
    <div class="brand"><span class="brand__mark"></span><span>VELMAR<br>CONSTRUCTION LLC</span></div>
  </section>

  <section class="card card--back" aria-label="Card back">
    <div class="contact">
      <p class="contact__name">Gerald Tomasino</p>
      <p class="contact__row">
        <svg class="icon" viewBox="0 0 18 18" aria-hidden="true"><rect x="2" y="4" width="14" height="10" fill="none" stroke="var(--orange)" stroke-width="1.4"/><path d="M2 4 L9 10 L16 4" fill="none" stroke="var(--orange)" stroke-width="1.4"/></svg>
        velmarllc@tridomail.com
      </p>
      <p class="contact__address">418 Harbor 87th.<br>Dunmoor Park, NY 10352</p>
      <div class="contact__phones">
        <p class="contact__row">
          <svg class="icon" viewBox="0 0 18 18" aria-hidden="true"><circle cx="9" cy="9" r="8" fill="none" stroke="var(--orange)" stroke-width="1.4"/><path d="M6 5 L7.6 5 L8.2 7 L7.2 8 C7.8 9.3 8.7 10.2 10 10.8 L11 9.8 L13 10.4 L13 12 C9 12.4 5.6 9 6 5 Z" fill="var(--orange)"/></svg>
          555-318-6094
        </p>
        <p class="contact__row">
          <svg class="icon" viewBox="0 0 18 18" aria-hidden="true"><circle cx="9" cy="9" r="8" fill="none" stroke="var(--orange)" stroke-width="1.4"/><rect x="6.5" y="4.5" width="5" height="9" rx="1" fill="none" stroke="var(--orange)" stroke-width="1.2"/></svg>
          555-742-0583
        </p>
      </div>
    </div>

    <div class="brand"><span class="brand__mark"></span><span>VELMAR<br>CONSTRUCTION LLC</span></div>

    <div class="web-band">
      <svg class="icon" viewBox="0 0 18 18" aria-hidden="true"><circle cx="9" cy="9" r="7.5" fill="none" stroke="var(--white)" stroke-width="1.4"/><ellipse cx="9" cy="9" rx="3.2" ry="7.5" fill="none" stroke="var(--white)" stroke-width="1.2"/><path d="M1.5 9 H16.5" stroke="var(--white)" stroke-width="1.2"/></svg>
      www.velmarllc.com
    </div>
  </section>

</body>
</html>
```